Brightwell Power Systems

We'd like a web design that's beautiful and professional. We replace existing inefficient systems (mostly lighting at the moment but expanding) with highly efficient systems.

```html
<!DOCTYPE html>
<html lang="en">
<head>
<meta charset="utf-8">
<title>Brightwell Power Systems</title>
<link rel="stylesheet" href="https://fonts.googleapis.com/css2?family=Open+Sans:wght@400;600;700&display=swap">
<style>
:root{
  --green:#1aaa5a;
  --green-dark:#12924b;
  --green-deep:#0d5a2a;
  --nav-green:#1a9a4e;
  --ink:#555;
  --heading:#666;
  --link:#1d4f8a;
  --footer-top:#444;
  --footer-bottom:#2a2a2a;
  --footer-bar:#222;
  --footer-text:#aaa;
  --white:#fff;
  --page:#f7f9f9;
}
*{box-sizing:border-box;margin:0;padding:0}
html,body{width:1150px;height:1200px;overflow:hidden}
body{position:relative;background:var(--page);font-family:"Open Sans",Arial,sans-serif;color:var(--ink)}
a{text-decoration:none;color:inherit}

/* header */
.site-header{position:absolute;left:0;top:0;width:1150px;height:72px;background:var(--white);border-top:3px solid var(--green);z-index:3}
.brand-box{position:absolute;left:145px;top:5px;width:151px;height:126px;background:var(--white);border-radius:4px;box-shadow:0 2px 8px rgba(0,0,0,.25);display:flex;flex-direction:column;align-items:center;justify-content:center;gap:8px;padding:0 12px;text-align:center}
.brand-mark{width:36px;height:36px;background:var(--green)}
.brand-name{font-size:15px;font-weight:600;color:var(--green-dark);line-height:1.2}
.main-nav{position:absolute;left:497px;top:34px;display:flex;gap:0;font-size:11.5px;letter-spacing:.5px;color:var(--nav-green)}
.main-nav a{position:absolute;white-space:nowrap}
.main-nav .caret{font-size:8px;margin-left:3px}
.header-social{position:absolute;left:898px;top:26px;display:flex;gap:13px}
.header-social span{width:25px;height:25px;border:2px solid #bbb;border-radius:3px}

/* hero */
.hero{position:absolute;left:0;top:72px;width:1150px;height:365px;background:linear-gradient(180deg,#3f87c9 0%,#7fb4de 45%,#c6dbea 68%,#8bbf55 82%,#4f8f2a 100%)}
.hero-title{position:absolute;left:157px;top:110px;width:540px;font-size:29px;line-height:32px;font-weight:700;color:#eef3f7;text-shadow:0 2px 3px rgba(0,0,0,.45)}
.hero-sub{position:absolute;left:157px;top:226px;font-size:16px;font-weight:600;color:#eef3f7;text-shadow:0 2px 3px rgba(0,0,0,.45)}
.hero-arrow{position:absolute;top:162px;width:40px;height:40px;border-radius:50%;border:3px solid rgba(255,255,255,.6);box-shadow:0 2px 5px rgba(0,0,0,.35);display:flex;align-items:center;justify-content:center}
.hero-arrow.prev{left:59px;background:var(--green)}
.hero-arrow.next{left:1052px;background:#3a3a3a}

/* feature band */
.features{position:absolute;left:0;top:437px;width:1150px;height:163px;background:var(--green);display:flex;justify-content:center;box-shadow:0 10px 14px -10px rgba(0,0,0,.35)}
.feature{width:287px;height:163px;text-align:center;color:var(--white);padding-top:22px;border-left:1px solid rgba(0,0,0,.12)}
.feature:first-child{border-left:none;width:287px}
.feature.active{background:#22b468}
.feature svg{display:block;margin:0 auto;height:66px}
.feature h3{font-size:22px;font-weight:400;margin-top:12px;line-height:26px}
.feature p{font-size:11px;text-transform:uppercase;margin-top:2px}

/* content */
.col{position:absolute;top:642px;width:270px}
.col h2{font-size:22px;font-weight:400;color:var(--heading)}
.col .photo{margin-top:14px;width:270px;height:112px}
.col p{margin-top:16px;font-size:11px;line-height:18px;color:#666;padding-left:3px}
.col .more{display:block;margin-top:24px;font-size:11.5px;color:var(--link)}
.news-title{display:block;margin-top:17px;font-size:15px;color:var(--link);text-decoration:underline}
.news-date{margin-top:6px;font-size:9px;color:#777;display:flex;align-items:center;gap:4px}
.col p.news-text{margin-top:14px;padding-left:0}

/* footer */
.site-footer{position:absolute;left:0;top:994px;width:1150px;height:165px;background:linear-gradient(180deg,var(--footer-top),var(--footer-bottom));border-top:2px solid #666}
.footer-brand{position:absolute;left:154px;top:26px;width:137px;height:113px;border:2px solid #111;display:flex;flex-direction:column;align-items:center;justify-content:center;gap:6px;padding:0 10px;text-align:center}
.footer-brand .brand-mark{width:28px;height:28px;background:var(--green-deep)}
.footer-brand .brand-name{color:var(--green-deep);font-size:13px}
.footer-col{position:absolute;top:32px}
.footer-col h4{font-size:13.5px;font-weight:700;color:var(--white)}
.footer-col ul{list-style:none;margin-top:12px}
.footer-col li{font-size:10px;color:var(--footer-text);height:21.5px;display:flex;align-items:center;gap:8px}
.footer-col li.current{color:#3d8fe0}
.tri{width:0;height:0;border-left:4px solid #888;border-top:3.5px solid transparent;border-bottom:3.5px solid transparent}
.contact li{height:27px;gap:12px}
.contact li.cont{padding-left:25px;height:20px}
.contact svg{width:13px;height:13px;flex:none}
.social-row{display:flex;gap:11px;margin-top:14px}
.social-row span{width:31px;height:31px;border-radius:3px;box-shadow:0 2px 3px rgba(0,0,0,.4)}
.footer-bar{position:absolute;left:0;top:1159px;width:1150px;height:41px;background:var(--footer-bar);font-size:10px;color:var(--footer-text)}
.footer-bar .copy{position:absolute;left:141px;top:14px}
.footer-bar .legal{position:absolute;left:873px;top:14px;display:flex;gap:10px}
</style>
</head>
<body>

<header class="site-header">
  <a class="brand-box" href="#">
    <span class="brand-mark"></span>
    <span class="brand-name">Brightwell Power Systems</span>
  </a>
  <nav class="main-nav">
    <a href="#" style="left:0">HOME</a>
    <a href="#" style="left:84px">ABOUT US<span class="caret">&#9660;</span></a>
    <a href="#" style="left:195px">SERVICES<span class="caret">&#9660;</span></a>
    <a href="#" style="left:304px">CONTACT</a>
  </nav>
  <div class="header-social"><span></span><span></span><span></span></div>
</header>

<section class="hero" role="img" aria-label="Transmission pylon under a blue sky above a green meadow">
  <h1 class="hero-title">Specialist Services in Electrical Engineering, Energy Management and Power Solutions</h1>
  <p class="hero-sub">Suspendisse tristique ante sit amet sem pulvinar posuere.</p>
  <a class="hero-arrow prev" href="#" aria-label="Previous"><svg width="8" height="10" viewBox="0 0 8 10"><path d="M6 1 2 5l4 4" fill="none" stroke="#fff" stroke-width="2"/></svg></a>
  <a class="hero-arrow next" href="#" aria-label="Next"><svg width="8" height="10" viewBox="0 0 8 10"><path d="M2 1l4 4-4 4" fill="none" stroke="#fff" stroke-width="2"/></svg></a>
</section>

<section class="features">
  <div class="feature">
    <svg viewBox="0 0 80 66" width="80">
      <rect x="3" y="2" width="74" height="54" fill="#3a3a3a"/>
      <g stroke="#8a8a8a" stroke-width="1.4">
        <path d="M3 13.5h74M3 25h74M3 36.5h74M3 48h74"/>
        <path d="M18 2v54M33 2v54M48 2v54M63 2v54"/>
      </g>
      <path d="M40 56v6H4" stroke="#3a3a3a" stroke-width="2" fill="none"/>
      <rect x="1" y="59" width="8" height="6" fill="#3a3a3a"/>
    </svg>
    <h3>Electrical Installation</h3>
    <p>Lorem ipsum dolor sit amet</p>
  </div>
  <div class="feature active">
    <svg viewBox="0 0 34 70" width="34">
      <path d="M14 0h16L20 26h10L10 70l5-34H4z" fill="#3a3a3a"/>
    </svg>
    <h3>Energy Management</h3>
    <p>Lorem ipsum dolor sit amet</p>
  </div>
  <div class="feature">
    <svg viewBox="0 0 70 66" width="70">
      <g fill="none" stroke="#3a3a3a" stroke-width="9">
        <path d="M22 24 32 8h8l8 12"/>
        <path d="M58 34l6 12-4 8H44"/>
        <path d="M24 56H10l-4-8 6-12"/>
      </g>
      <path d="M42 16l14 2-6 12z" fill="#3a3a3a"/>
      <path d="M46 62l-10-8 10-8z" fill="#3a3a3a"/>
      <path d="M6 32l8-12 6 12z" fill="#3a3a3a"/>
    </svg>
    <h3>Renewable Energy</h3>
    <p>Lorem ipsum dolor sit amet</p>
  </div>
</section>

<section class="col" style="left:153px">
  <h2>About Us</h2>
  <div class="photo" role="img" aria-label="City skyline of office towers under a blue sky" style="background:linear-gradient(180deg,#2f5fb3 0%,#3f6fc0 45%,#1f3f7a 100%)"></div>
  <p>Lid est laborum dolo rumes fugats untras. Etharums ser quidem rerum facilis dolores nemis omnis fugats vitaes nemo minima rerums unsers</p>
  <a class="more" href="#">Learn More &nbsp;&#8250;</a>
</section>

<section class="col" style="left:440px">
  <h2>Our Services</h2>
  <div class="photo" role="img" aria-label="Power line towers at sunset" style="background:linear-gradient(180deg,#9fb8cf 0%,#e8c7a2 45%,#d79a5a 70%,#4a3a2a 100%)"></div>
  <p>Lid est laborum dolo rumes fugats untras. Etharums ser quidem rerum facilis dolores nemis omnis fugats vitaes nemo minima rerums unsers</p>
  <a class="more" href="#">Learn More &nbsp;&#8250;</a>
</section>

<section class="col" style="left:729px">
  <h2>Latest News</h2>
  <div class="photo" role="img" aria-label="Business team silhouetted against bright office windows" style="background:linear-gradient(90deg,#c8d6e6 0%,#6e86a6 30%,#dce6f0 55%,#5c7396 80%,#d0dcea 100%)"></div>
  <a class="news-title" href="#">The Top 10 Best Electrical Companies</a>
  <div class="news-date"><svg width="9" height="9" viewBox="0 0 9 9"><rect x=".5" y="1.5" width="8" height="7" fill="none" stroke="#999"/><path d="M.5 3.5h8" stroke="#999"/></svg>8 December 2013</div>
  <p class="news-text">The point of using Lorem Ipsum is that it has a more-or-less normal distribution of letters, as opposed to using..</p>
</section>

<footer class="site-footer">
  <div class="footer-brand">
    <span class="brand-mark"></span>
    <span class="brand-name">Brightwell Power Systems</span>
  </div>
  <div class="footer-col" style="left:360px">
    <h4>Navigation</h4>
    <ul>
      <li><span class="tri"></span>Home</li>
      <li><span class="tri"></span>About</li>
      <li><span class="tri"></span>Services</li>
      <li><span class="tri"></span>Contact</li>
    </ul>
  </div>
  <div class="footer-col" style="left:504px">
    <h4>Services</h4>
    <ul>
      <li class="current"><span class="tri"></span>Menu1</li>
      <li><span class="tri"></span>Menu1</li>
      <li><span class="tri"></span>Menu1</li>
      <li><span class="tri"></span>Menu1</li>
    </ul>
  </div>
  <div class="footer-col contact" style="left:647px">
    <h4>Contact Us</h4>
    <ul>
      <li><svg viewBox="0 0 13 13"><path d="M3 1l2 3-1.5 1.5c1 2 2 3 4 4L9 8l3 2-1.5 2C6 12 1 7 1 2.5z" fill="#999"/></svg>+1 800-555-0142</li>
      <li><svg viewBox="0 0 13 13"><rect x="1" y="3" width="11" height="7" fill="#999"/><path d="M1 3l5.5 4L12 3" fill="none" stroke="#444"/></svg>hello@brightwellpower.example</li>
      <li><svg viewBox="0 0 13 13"><path d="M6.5 1a3.8 3.8 0 0 1 3.8 3.8c0 3-3.8 7.2-3.8 7.2S2.7 7.8 2.7 4.8A3.8 3.8 0 0 1 6.5 1z" fill="#999"/><circle cx="6.5" cy="4.8" r="1.4" fill="#444"/></svg>Your Address, Your Country</li>
      <li class="cont">Your Zip Code</li>
    </ul>
  </div>
  <div class="footer-col" style="left:841px">
    <h4>Social</h4>
    <div class="social-row">
      <span style="background:#3b5b9a"></span>
      <span style="background:#2aa6e0"></span>
      <span style="background:#1a6d9e"></span>
      <span style="background:#d2352a"></span>
    </div>
  </div>
</footer>

<div class="footer-bar">
  <span class="copy">Copyright 2014 &copy; CompanyName - All Rights Reserved</span>
  <span class="legal"><a href="#">Site Map</a><span>&#9642;</span><a href="#">Privacy Policy</a></span>
</div>

</body>
</html>
```